DELVANE ROOFING YARD SIGN

We need a yard sign to put in our customers' yards when we are roofing their home.
Delvane Roofing
468 Pettigrew Rd
Marrow Bend LA 70452
phone: 337-555-0148

Maybe some verbiage like "Your Hometown Roofing Experts"
or
"Family Owned Since 1962"

```html
<!DOCTYPE html>
<html lang="en">
<head>
<meta charset="utf-8">
<title>Delvane Roofing Yard Sign</title>
<link rel="stylesheet" href="https://fonts.googleapis.com/css2?family=Montserrat:wght@700;800;900&display=swap">
<style>
  :root {
    --bg: #dfe6ec;
    --frame: #8c8d8f;
    --ink: #111111;
    --panel: #141414;
    --silver-light: #e4e4e4;
    --silver-mid: #bdbdbd;
    --silver-dark: #8f8f8f;
    --headline: #cfcfcf;
    --badge: #f4f4f2;
  }
  * { box-sizing: border-box; margin: 0; padding: 0; }
  html, body { width: 1200px; height: 1200px; overflow: hidden; }
  body {
    background: var(--bg);
    font-family: "Montserrat", Arial, sans-serif;
    position: relative;
  }
  .yard-sign {
    position: absolute;
    left: 100px; top: 160px;
    width: 1000px; height: 880px;
    background: var(--frame);
    padding: 12px;
  }
  .sign-face {
    position: relative;
    width: 100%; height: 100%;
    background: var(--panel);
    overflow: hidden;
  }
  .top-band { position: absolute; left: 0; top: 0; width: 100%; height: 105px; background: var(--panel); }
  .brand-band {
    position: absolute; left: 0; top: 105px; width: 100%; height: 160px;
    background: linear-gradient(90deg, var(--silver-dark), var(--silver-light) 45%, var(--silver-mid) 70%, var(--silver-light));
  }
  .brand-badge {
    position: absolute; left: 50%; top: 40px;
    width: 310px; height: 310px; margin-left: -155px;
    border-radius: 50%;
    background: var(--badge);
    border: 6px solid var(--silver-mid);
    display: flex; align-items: center; justify-content: center;
    text-align: center;
  }
  .brand-name {
    font-weight: 800; font-size: 34px; line-height: 1.15;
    letter-spacing: 2px; color: var(--ink);
  }
  .headline {
    position: absolute; left: 0; top: 385px; width: 100%;
    text-align: center;
    font-weight: 900; font-size: 84px; line-height: 92px;
    color: var(--headline); letter-spacing: 1px;
  }
  .tagline {
    position: absolute; left: 0; top: 580px; width: 100%;
    display: flex; align-items: center; justify-content: center; gap: 22px;
    font-weight: 800; font-size: 31px; letter-spacing: 4px; color: var(--headline);
  }
  .tagline .rule { width: 100px; height: 3px; background: var(--headline); }
  .contact-band {
    position: absolute; left: 0; top: 650px; width: 100%; height: 206px;
    background: linear-gradient(90deg, var(--silver-mid), var(--silver-light) 40%, var(--silver-mid) 75%, var(--silver-light));
    text-align: center;
  }
  .phone {
    margin-top: 30px;
    display: flex; align-items: center; justify-content: center; gap: 22px;
    font-weight: 900; font-size: 92px; line-height: 1; color: var(--ink);
  }
  .phone svg { width: 84px; height: 84px; }
  .address {
    margin-top: 26px;
    font-weight: 800; font-size: 28px; letter-spacing: 2px; color: var(--ink);
  }
</style>
</head>
<body>
  <div class="yard-sign">
    <div class="sign-face">
      <div class="top-band"></div>
      <div class="brand-band"></div>
      <div class="brand-badge">
        <span class="brand-name">DELVANE<br>ROOFING</span>
      </div>
      <h1 class="headline">YOUR HOMETOWN<br>ROOFING EXPERTS</h1>
      <p class="tagline"><span class="rule"></span>FAMILY OWNED SINCE 1962<span class="rule"></span></p>
      <div class="contact-band">
        <p class="phone">
          <svg viewBox="0 0 24 24" aria-hidden="true">
            <circle cx="12" cy="12" r="12" fill="#111"/>
            <path fill="#d8d8d8" d="M8.2 5.6c.4-.1.8 0 1 .4l1.2 2.4c.2.4.1.8-.2 1.1l-1 1c.7 1.5 1.9 2.7 3.4 3.4l1-1c.3-.3.7-.4 1.1-.2l2.4 1.2c.4.2.5.6.4 1l-.5 1.8c-.1.4-.5.7-.9.7C10.6 17.4 6.6 13.4 6.6 8c0-.4.3-.8.7-.9z"/>
          </svg>
          337-555-0148
        </p>
        <p class="address">468 PETTIGREW RD MARROW BEND LA 70452</p>
      </div>
    </div>
  </div>
</body>
</html>
```